New Business Card Design for Engineering and Surveying Company

We need a new design template for our business cards. We are a civil engineering, land surveying and pipeline integrity business. Please see dkhpartners.com for details. We need a bold, new business card design to complement our rebranding and marketing program. We have anew logo and attached vectro file. Please find additional details below. I am available to answer any questions.

Target Market(s)

Contractors, business owners, oil companies

Contact Information for Business Card

Needs to be customizable for different people (name, title, cell)

Font styles to use
Sans Serif
Other font styles liked:
• See eps file

Requirements
Must have
• Example Information:
Trevor Ashcombe

T:409-555-0173
M: 202-555-0148
tashcombe@dkhprtnrs.com

Address: 1875 Pinecrest Parkway, Corvale, Texas 70990
Email: tolvanrey@dkhpartners.com
Website: www.dkhpartners.com
Nice to have
• I would like the back of the card to have the logo on a bold background with the text below:

[logo]
DORAN KESSLING & PARTNERS
CIVIL ENGINEERING | LAND SURVEYING | PIPELINE INTEGRITY

The reverse side should have the contact information for the person (example above), a smaller version of the logo and a graphic

```html
<!DOCTYPE html>
<html lang="en">
<head>
<meta charset="utf-8">
<title>Doran Kessling &amp; Partners — Business Card</title>
<link href="https://fonts.googleapis.com/css2?family=Montserrat:wght@500;700;800&family=Roboto:wght@400;500;700&display=swap" rel="stylesheet">
<style>
  :root {
    --backdrop: #c9c9c9;
    --card-dark: #141414;
    --card-light: #f7f7f7;
    --ink: #1a1a1a;
    --white: #ffffff;
    --accent-red: #d3242b;
    --accent-blue: #2b3a8f;
    --muted-light: #d6d6d6;
  }
  * { box-sizing: border-box; margin: 0; padding: 0; }
  html, body { width: 1200px; height: 852px; overflow: hidden; }
  body {
    background: var(--backdrop);
    font-family: "Roboto", Arial, sans-serif;
    position: relative;
  }
  .card {
    position: absolute;
    width: 540px;
    height: 309px;
    border-radius: 16px;
    top: 272px;
    overflow: hidden;
  }
  /* Front: bold background with brand */
  .card-front {
    left: 40px;
    background: var(--card-dark);
    color: var(--white);
  }
  .brand {
    position: absolute;
    left: 110px;
    top: 70px;
    display: flex;
    align-items: center;
    gap: 18px;
  }
  .brand-square {
    width: 34px;
    height: 34px;
    background: var(--accent-red);
  }
  .brand-name {
    font-family: "Montserrat", Arial, sans-serif;
    font-weight: 800;
    font-size: 84px;
    line-height: 1;
    letter-spacing: 2px;
  }
  .brand-front .brand-name { color: var(--white); }
  .company-name {
    position: absolute;
    left: 162px;
    top: 164px;
    font-family: "Montserrat", Arial, sans-serif;
    font-weight: 700;
    font-size: 14.5px;
    letter-spacing: 0.6px;
  }
  .services {
    position: absolute;
    left: 0;
    right: 0;
    bottom: 56px;
    text-align: center;
    font-family: "Montserrat", Arial, sans-serif;
    font-weight: 500;
    font-size: 13px;
    letter-spacing: 0.8px;
    color: var(--muted-light);
  }
  .services .divider { color: var(--accent-red); margin: 0 8px; }

  /* Back: contact side */
  .card-back {
    left: 620px;
    background: var(--card-light);
    color: var(--ink);
  }
  .brand-back {
    left: auto;
    right: 44px;
    top: 34px;
    gap: 12px;
  }
  .brand-back .brand-square { width: 22px; height: 22px; }
  .brand-back .brand-name { font-size: 50px; color: var(--ink); }
  .rule-main {
    position: absolute;
    left: 150px;
    right: 30px;
    top: 112px;
    height: 1.5px;
    background: linear-gradient(90deg, var(--accent-blue), var(--accent-red));
  }
  .person {
    position: absolute;
    left: 34px;
    top: 142px;
  }
  .person-name {
    font-weight: 700;
    font-size: 21px;
    color: var(--accent-blue);
  }
  .person-title {
    font-size: 14px;
    margin-top: 3px;
  }
  .rule-person {
    position: absolute;
    left: 34px;
    top: 197px;
    width: 160px;
    height: 1.5px;
    background: var(--accent-blue);
  }
  .contacts {
    position: absolute;
    left: 34px;
    top: 206px;
    list-style: none;
    font-size: 14px;
  }
  .contacts li {
    display: flex;
    align-items: center;
    gap: 10px;
    height: 21px;
  }
  .contacts svg { width: 12px; height: 12px; fill: var(--accent-red); flex: none; }
  .address {
    position: absolute;
    right: 34px;
    top: 148px;
    text-align: right;
    font-size: 14px;
    line-height: 1.55;
  }
</style>
</head>
<body>

<section class="card card-front" aria-label="Card front">
  <div class="brand brand-front">
    <span class="brand-square"></span>
    <span class="brand-name">DKP</span>
  </div>
  <p class="company-name">DORAN KESSLING &amp; PARTNERS</p>
  <p class="services">CIVIL ENGINEERING<span class="divider">|</span>LAND SURVEYING<span class="divider">|</span>PIPELINE INTEGRITY</p>
</section>

<section class="card card-back" aria-label="Card back">
  <div class="brand brand-back">
    <span class="brand-square"></span>
    <span class="brand-name">DKP</span>
  </div>
  <div class="rule-main"></div>

  <div class="person">
    <p class="person-name">Trevor Ashcombe</p>
    <p class="person-title">Chief Executive Officer</p>
  </div>
  <div class="rule-person"></div>

  <ul class="contacts">
    <li>
      <svg viewBox="0 0 24 24" aria-hidden="true"><path d="M6.6 10.8a15 15 0 0 0 6.6 6.6l2.2-2.2a1 1 0 0 1 1-.25 11.4 11.4 0 0 0 3.6.57 1 1 0 0 1 1 1V20a1 1 0 0 1-1 1A17 17 0 0 1 3 4a1 1 0 0 1 1-1h3.5a1 1 0 0 1 1 1c0 1.25.2 2.45.57 3.6a1 1 0 0 1-.25 1z"/></svg>
      409-555-0173
    </li>
    <li>
      <svg viewBox="0 0 24 24" aria-hidden="true"><path d="M6.6 10.8a15 15 0 0 0 6.6 6.6l2.2-2.2a1 1 0 0 1 1-.25 11.4 11.4 0 0 0 3.6.57 1 1 0 0 1 1 1V20a1 1 0 0 1-1 1A17 17 0 0 1 3 4a1 1 0 0 1 1-1h3.5a1 1 0 0 1 1 1c0 1.25.2 2.45.57 3.6a1 1 0 0 1-.25 1z"/></svg>
      202-555-0148
    </li>
    <li>
      <svg viewBox="0 0 24 24" aria-hidden="true"><path d="M2 5h20v14H2zM4 7v.4l8 5 8-5V7l-8 5z"/></svg>
      tashcombe@dkhprtnrs.com
    </li>
    <li>
      <svg viewBox="0 0 24 24" aria-hidden="true"><circle cx="12" cy="12" r="10"/></svg>
      www.dkhpartners.com
    </li>
  </ul>

  <p class="address">1875 Pinecrest Parkway,<br>Corvale, Texas 70990</p>
</section>

</body>
</html>
```